GustHarbor.com - migration and redesign

******Updated Nov. 17th, 2014******

Our current site is on the PLOM platform. We want to redesign it using Wordpress. We are very open to graphic enhancements. Must be a responsive. Home page needs some sort of social feed aggregator that displays content posts from all our social networks.

www.gustharbor.com

Project Scope:
Graphic design
UX
WordPress Installation (including all required enhancements.

The home page of the site should be built using a social aggregator add-in similar to what is running on the live site.

For all ads AD Use KVR DOS standard sizes.: http://www.kvr-example.net/guidelines/508676/508767/displayguidelines

At the very least:
Leaderboard AD in the header/Footer of the site (728x90)
Wide skyscraper (160x600) (on secondary pages)

GustHarbor is a hobby site. We've been around for a long time. Your design will get noticed!!!

Check out Oldpages.org ( https://web.oldpages-example.org/web/*/http://www.gustharbor.com ) there you can see how long we've been operating and get a sence for who we are.

Here are some sites we like for inspiration:

http://www.brimwayfarer.com
http://www.tumvex.com/us/en
http://www.pimsoltek.de

About GustHarbor.com:

GustHarbor is one of the longest running website for thrill seekers around the globe. Since its introduction to the World Wide Web in 2001, GustHarbor has become the place for thrill seekers to "Sit down, log in, and hang on!" as they exchange news, rumors, tips, and information about the amusement park industry. Whether it be roller coasters, theme parks, water slides, or other extreme thrill attractions, GustHarbor is a community where the adrenaline-minded can connect and share the excitement of always being on the edge. We are proud to have over 12,000 members who have been active within the amusement industry. We have incredibly knowledgeable members that have worked in the industry and some even have engineering degrees.
Updates

Thank you for helping us out. I've updated with SOW/Brief to include more specifics. Let me know if you have any questions. Thanks! Dorn

Hello - Thanks for these great designs. Solid starts but you're not following the guidelines set out in the design brief. Specifically: *********FROM THE BRIEF******** The home page of the site should be built using a social aggregator add-in similar to what is running on the live site. For all ads AD Use KVR DOS standard sizes.: http://www.kvr-example.net/guidelines/508676/508767/displayguidelines At the very least: Leaderboard AD in the header/Footer of the site (728x90) Wide skyscraper (160x600) (on secondary pages) *********FROM THE BRIEF******** Let me know if you have questions about this. Thanks. Dorn

Project Deadline Extended
Reason: We only received one submission that actually bothered to read and follow the design brief. Thanks! Dorn

Target Market(s)

Fans of all things thrill related but focusing on Amusement Parks and Roller Coasters.

Industry/Entity Type

Amusement Park

Font styles to use
Sans Serif

Requirements
Must have
• Responsive Design
Blog/Articles
Social Aggregator
SEO optimized
Plexo Admint Ads
Contact Us Form
Newsletter Sign-up
Social log in and sharing
Chatterly comments on articles
Wordpress comments on articles
Feel free to use Plexo Glyph ( http://www.plexo-example.com/fonts )
Should not have
• Copyrighted photos. Please use open source images. Please do not use protected fonts.

```html
<!DOCTYPE html>
<html lang="en">
<head>
<meta charset="utf-8">
<title>GustHarbor.com – Home</title>
<link rel="stylesheet" href="https://fonts.googleapis.com/css2?family=Open+Sans:wght@400;600;700&display=swap">
<style>
:root{
  --navy:#1b2748;
  --navy-deep:#16213d;
  --blue:#1f6fb5;
  --blue-soft:#c8dbef;
  --red:#c9302c;
  --ink:#222;
  --muted:#888;
  --line:#dcdcdc;
  --page:#f3f3f3;
  --white:#fff;
  --nav:#e6e6e6;
  --footer:#2b2b2b;
  --band:#8c8c8c;
  --news-blue:#2a7ac0;
}
*{box-sizing:border-box;margin:0;padding:0}
html,body{width:1200px;height:3594px;overflow:hidden}
body{position:relative;background:var(--page);font-family:"Open Sans",Arial,sans-serif;color:var(--ink);font-size:13px}
a{color:inherit;text-decoration:none}
.abs{position:absolute}

.topbar{left:0;top:0;width:1200px;height:34px;background:var(--navy)}
.topbar .links{position:absolute;left:40px;top:9px;color:#fff;font-size:12px;display:flex;gap:24px}
.topbar .icons{position:absolute;right:32px;top:6px;display:flex;gap:6px}
.sq{display:inline-block;width:22px;height:22px;border-radius:2px}

.header{left:0;top:34px;width:1200px;height:140px;background:var(--white)}
.brand{position:absolute;left:58px;top:44px;display:flex;align-items:center;gap:12px;font-size:34px;font-weight:700;color:var(--navy)}
.brand .dot{width:30px;height:30px;background:var(--red)}
.lead-ad{position:absolute;left:470px;top:30px;width:690px;height:90px;background:linear-gradient(90deg,#f7d94c,#f2c21c);display:flex;align-items:center;padding:0 20px;gap:20px;font-weight:700;color:#1a1a1a}
.lead-ad .tag{background:var(--navy);color:#fff;padding:6px 10px;font-size:14px}
.lead-ad .pic{flex:1;height:60px;background:linear-gradient(90deg,#d6b23a,#8c7a3c);border-radius:4px}
.lead-ad .off{font-size:30px;color:var(--red)}
.lead-ad .buy{background:var(--red);color:#fff;padding:8px 14px;font-size:13px}

.nav{left:33px;top:174px;width:1134px;height:52px;background:var(--nav);border:1px solid var(--line);display:flex;align-items:center}
.nav .home{width:52px;height:52px;background:#3c3c3c}
.nav ul{list-style:none;display:flex}
.nav li{padding:0 14px;font-size:13px;font-weight:600;text-transform:uppercase;color:#333;border-right:1px solid #ccc}
.nav .tools{margin-left:auto;display:flex;gap:10px;padding-right:10px}
.nav .tools span{width:30px;height:30px;background:#cfcfcf}

.box{position:absolute;background:var(--white);border:1px solid var(--line);padding:14px 16px}
.box h3{display:flex;align-items:center;gap:10px;font-size:13px;font-weight:700;color:var(--blue);text-transform:uppercase;margin-bottom:14px}
.box h3::after{content:"";flex:1;height:10px;background:var(--blue-soft)}
.meta{font-size:10px;color:var(--muted)}
.more{color:var(--red);font-size:11px;font-weight:600}
.showmore{position:absolute;left:0;right:0;bottom:0;height:38px;border-top:1px solid var(--line);text-align:center;line-height:38px;font-size:12px;color:#555}
.ph{display:block;border-radius:1px}

.slider{left:33px;top:262px;width:620px;height:498px;padding:18px}
.slider .main{width:584px;height:408px;background:linear-gradient(160deg,#8fb3d8 0%,#b9cfe2 40%,#d1a52c 60%,#6d7a3a 100%)}
.slider .thumbs{display:flex;gap:8px;margin-top:8px}
.slider .thumbs span{flex:1;height:54px;background:linear-gradient(#7aa2c8,#5b6e3a)}

.recent{left:33px;top:802px;width:620px;height:718px}
.post{display:flex;gap:16px;height:152px;padding-top:10px;border-bottom:1px solid #eee;position:relative}
.post .ph{width:183px;height:118px;flex:none}
.post h4{font-size:14px;font-weight:600;margin-bottom:4px}
.post p{font-size:11px;color:#666;line-height:1.5;width:300px}
.share{position:absolute;right:0;top:10px;width:70px}
.share .icons{display:grid;grid-template-columns:repeat(3,22px);gap:2px}
.share .views{background:#333;color:#fff;font-size:9px;padding:2px 4px;margin-top:2px}

.news{left:33px;top:1543px;width:620px;height:447px}
.news .lead{position:absolute;left:16px;top:48px;width:270px}
.news .lead .ph{width:270px;height:170px;background:linear-gradient(135deg,#c9a36a,#7b5a2e)}
.news .lead h4{font-size:15px;font-weight:600;margin:12px 0 4px}
.news .lead p{font-size:11px;color:#666;line-height:1.5}
.news .list{position:absolute;left:310px;top:48px;width:290px}
.news .item{display:flex;gap:14px;margin-bottom:16px;height:70px}
.news .item .ph{width:84px;height:60px;flex:none}
.news .item h4{font-size:12px;font-weight:400;margin-bottom:4px}

.half{top:2013px;width:300px;height:489px}
.leisure{left:33px}
.tech{left:353px}
.half .ph{width:266px;height:160px}
.half h4{font-size:14px;font-weight:600;margin:14px 0 6px}
.half p{font-size:11px;color:#666;line-height:1.5}

.latest{left:672px;top:262px;width:495px;height:250px}
.latest h4{font-size:15px;font-weight:700;margin-bottom:10px}
.latest .row{display:flex;gap:14px}
.latest .ph{width:140px;height:100px;flex:none;background:linear-gradient(#b34a4a,#e0b080)}
.latest p{font-size:11px;color:#555;line-height:1.5}
.featured{left:672px;top:540px;width:191px;height:470px;padding:14px 10px}
.featured .ph{width:170px;height:120px}
.featured h4{font-size:11px;font-weight:400;margin:6px 0 2px}
.featured .gap{margin-bottom:14px}
.advert{left:672px;top:1037px;width:191px;height:650px;padding:14px 10px}
.sky{width:160px;height:560px;margin:0 auto;background:linear-gradient(#1e5aa8 0%,#3a78c4 45%,#e8eef5 75%,#c9d3dd 100%);color:#fff;padding:120px 10px 0;text-align:center}
.sky strong{display:block;font-size:18px;line-height:1.2}
.sky span{display:block;font-size:11px;margin-top:10px}
.sky .btn{display:inline-block;margin-top:12px;background:#fff;color:#1e5aa8;font-size:10px;font-weight:700;padding:4px 8px}
.archive{left:672px;top:1714px;width:191px;height:236px;padding:14px 10px}
.archive li{list-style:none;display:flex;justify-content:space-between;font-size:11px;color:#444;padding:4px 0;border-bottom:1px solid #f0f0f0}
.tweets{left:672px;top:1969px;width:191px;height:533px;padding:0;overflow:hidden}
.tweets .hint{background:#3f8ac7;color:#fff;font-size:10px;padding:8px;text-align:center;line-height:1.4}
.tweets .head{display:flex;justify-content:space-between;padding:8px;font-size:12px;font-weight:700;color:var(--blue);border-bottom:1px solid #eee}
.tweet{padding:8px;font-size:10px;color:#444;border-bottom:1px solid #eee;line-height:1.4}
.tweet b{color:#222}
.tweet .tag{color:var(--blue)}
.tweets .compose{position:absolute;bottom:0;left:0;right:0;padding:8px;font-size:10px;border-top:1px solid #ddd;background:#fafafa}

.video{left:879px;top:540px;width:288px;height:260px}
.video .ph{width:254px;height:170px;background:linear-gradient(#2a2a2a,#6b1e1e)}
.login{left:879px;top:815px;width:288px;height:208px}
.field{display:flex;height:32px;border:1px solid #ccc;margin-bottom:10px}
.field i{width:30px;background:#eee}
.field span{padding:7px;font-size:11px;color:#aaa}
.login .act{display:flex;align-items:center;gap:30px;font-size:11px;color:#555}
.login .btn{background:var(--red);color:#fff;padding:6px 14px;font-size:12px}
.counter{left:879px;top:1050px;width:288px;height:291px}
.counter .grid{display:grid;grid-template-columns:repeat(3,1fr);border:1px solid #eee}
.counter .cell{height:74px;border:1px solid #eee;text-align:center;padding-top:8px;font-size:10px;color:#666}
.counter .cell i{display:block;width:18px;height:18px;margin:0 auto 4px}
.comments{left:879px;top:1363px;width:288px;height:627px}
.cm{display:flex;gap:10px;margin-bottom:16px;height:60px}
.cm .ph{width:70px;height:48px;flex:none}
.cm h4{font-size:11px;font-weight:400;line-height:1.4}
.follow{left:879px;top:2013px;width:288px;height:157px}
.follow .grid{display:grid;grid-template-columns:repeat(7,30px);gap:6px}
.follow .grid span{height:30px}
.fb{left:879px;top:2193px;width:288px;height:309px}
.fbcard{border:1px solid #ddd;padding:10px;font-size:11px}
.fbcard .top{display:flex;gap:8px;margin-bottom:10px}
.fbcard .top i{width:40px;height:40px;background:#ddd}
.faces{display:grid;grid-template-columns:repeat(4,1fr);gap:6px;margin-top:8px}
.faces span{height:44px;background:#c9c9c9}

.feed{left:33px;top:2530px;width:1134px;height:400px;padding:0;overflow:hidden}
.feed .bar{background:#4a64a0;color:#fff;font-size:12px;font-weight:700;padding:6px 10px}
.feed .page{display:flex;gap:10px;padding:10px;font-size:11px}
.feed .page i{width:40px;height:40px;background:#ddd}
.feed .post{display:block;height:auto;border:0;margin:0 10px;padding:10px;border-top:1px solid #ddd;font-size:14px}
.feed .post .ph{width:500px;height:240px;margin-top:12px;background:linear-gradient(#9ec3e6,#d8e6f2 70%,#8a8a8a)}

.band{left:0;top:2945px;width:1200px;height:649px;background:var(--band)}
.foot-ad{left:250px;top:2968px;width:700px;height:90px;background:#fff;display:flex;align-items:center;padding:0 16px;gap:20px;font-weight:700;font-size:13px}
.foot-ad .bags{flex:1;height:64px;background:linear-gradient(90deg,#2c4aa8,#c02a5a)}
.newsletter{left:33px;top:3070px;width:1134px;height:150px;background:var(--news-blue);padding:24px 32px;color:#fff}
.newsletter h2{font-size:24px;font-weight:400;margin-bottom:12px}
.newsletter .row{display:flex;gap:40px}
.newsletter .in{width:880px;height:44px;background:#fff;color:#aaa;padding:12px 14px;font-size:13px}
.newsletter .go{background:var(--red);width:150px;height:44px;text-align:center;line-height:44px;font-size:15px}
.footer{left:33px;top:3220px;width:1134px;height:338px;background:var(--footer);color:#ccc;padding:30px 28px;display:flex;gap:40px}
.footer h5{color:#fff;font-size:14px;margin-bottom:14px;text-transform:uppercase}
.footer p,.footer li{font-size:11px;line-height:1.6;list-style:none}
.footer .about{width:270px}
.footer .links{width:230px}
.footer .contact{width:260px}
.footer .contact span{display:block;height:26px;background:#555;margin-bottom:8px;font-size:10px;color:#999;padding:5px}
.footer .contact .msg{height:100px}
.footer .contact .btn{width:80px;height:28px;background:var(--red);color:#fff;text-align:center;line-height:28px;font-size:12px;margin-left:180px}
.footer .follows .grid{display:flex;gap:8px}
.footer .follows .grid span{width:22px;height:22px;background:#ddd}
.bottom{left:0;top:3558px;width:1200px;height:36px;background:var(--navy-deep);color:#aaa;font-size:11px;padding:10px 40px}
.totop{right:44px;top:3495px;width:50px;height:50px;background:#1a1a1a}
</style>
</head>
<body>

<div class="abs topbar">
  <div class="links"><a>Roller Coaster History</a><a>Timeline of Roller Coasters and Thrillrides</a><a>Glossary of Roller Coaster Terms</a></div>
  <div class="icons"><span class="sq" style="background:#3aa0e0"></span><span class="sq" style="background:#3b5998"></span><span class="sq" style="background:#d94a38"></span><span class="sq" style="background:#c4302b"></span><span class="sq" style="background:#f08a24"></span><span class="sq" style="background:#0063dc"></span></div>
</div>

<header class="abs header">
  <div class="brand"><span class="dot"></span>GustHarbor</div>
  <div class="lead-ad"><span class="tag">DEAL SAGE</span><span class="pic" role="img" aria-label="Sunglasses product photo"></span><span class="off">80% OFF</span><span>on Sunglasses</span><span class="buy">Buy now</span></div>
</header>

<nav class="abs nav">
  <span class="home"></span>
  <ul><li>About</li><li>Midway</li><li>Articles</li><li>News</li><li>Technology</li><li>Videos</li><li>Photos</li><li>Art &amp; Entertainment</li><li>Leisure</li></ul>
  <div class="tools"><span></span><span></span></div>
</nav>

<section class="box slider">
  <div class="ph main" role="img" aria-label="Yellow roller coaster loop against a blue sky"></div>
  <div class="thumbs"><span></span><span></span><span></span><span></span><span></span><span></span><span></span></div>
</section>

<section class="box recent">
  <h3>Recent Posts</h3>
  <article class="post"><span class="ph" role="img" aria-label="Family ride construction" style="background:linear-gradient(#a9c3da,#7b8c5a)"></span><div><h4>MASON, Ohio – Two new family rides</h4><div class="meta">November 6, 2014</div><p>MASON, Ohio – Two new family rides, the largest Beanpoint store in the Tri State, and other improvements are all part of Crown Ridge's… <span class="more">Read More »</span></p></div><div class="share"><div class="icons"><span class="sq" style="background:#3b5998"></span><span class="sq" style="background:#3aa0e0"></span><span class="sq" style="background:#333"></span></div><div class="views">Views: 150</div></div></article>
  <article class="post"><span class="ph" role="img" aria-label="Coaster track at dusk" style="background:linear-gradient(#e7a35a,#3b3b55)"></span><div><h4>The base of the lift of #Gale410 is ready</h4><div class="meta">October 21, 2014</div><p>The base of the lift of #Gale410 is ready for more track! Brake run and station sections are coming along nicely. <span class="more">Read More »</span></p></div><div class="share"><div class="icons"><span class="sq" style="background:#3b5998"></span><span class="sq" style="background:#3aa0e0"></span><span class="sq" style="background:#333"></span></div><div class="views">Views: 98</div></div></article>
  <article class="post"><span class="ph" role="img" aria-label="Ride at night" style="background:linear-gradient(#2b1a12,#8a3a1a)"></span><div><h4>It has been done. 50 million rides</h4><div class="meta">October 20, 2014</div><p>It has been done. 50 million rides! pic.link/ride50m <span class="more">Read More »</span></p></div><div class="share"><div class="icons"><span class="sq" style="background:#3b5998"></span><span class="sq" style="background:#3aa0e0"></span><span class="sq" style="background:#333"></span></div><div class="views">Views: 77</div></div></article>
  <article class="post" style="border:0"><span class="ph" role="img" aria-label="Fright farm event poster" style="background:#1a1a1a"></span><div><h4>Ted Zolar visits Knoll's Fright Farm Haunt</h4><div class="meta">October 16, 2014</div><p>The best, biggest, and the original haunt in town decided to try something entirely new this year… <span class="more">Read More »</span></p></div><div class="share"><div class="icons"><span class="sq" style="background:#3b5998"></span><span class="sq" style="background:#3aa0e0"></span><span class="sq" style="background:#333"></span></div><div class="views">Views: 64</div></div></article>
  <div class="showmore">Show More</div>
</section>

<section class="box news">
  <h3>News</h3>
  <div class="lead"><span class="ph" role="img" aria-label="Plate of comfort food"></span><h4>Comfort Food Hidden Gems at Walt Dreamvale</h4><p>As the weather cools down, I begin to crave comfort food. We all have a favorite food… <span class="more">Read More »</span></p></div>
  <div class="list">
    <div class="item"><span class="ph" role="img" aria-label="Movie character" style="background:#b9b0a4"></span><div><h4>It was a super weekend for Big Robo 7</h4><span class="more">Read more »</span></div></div>
    <div class="item"><span class="ph" role="img" aria-label="Coaster close-up" style="background:#a35c3c"></span><div><h4>Bump In The Night #65 by vantrel</h4><span class="more">Read more »</span></div></div>
    <div class="item"><span class="ph" role="img" aria-label="Comic scene" style="background:#3a6aa0"></span><div><h4>Go Back To Work With Perry Packer</h4><span class="more">Read more »</span></div></div>
    <div class="item"><span class="ph" role="img" aria-label="Holiday run crowd" style="background:#6a8a5a"></span><div><h4>First ever Hollow Run a success</h4><span class="more">Read more »</span></div></div>
  </div>
  <div class="showmore">Show More</div>
</section>

<section class="box half leisure">
  <h3>Leisure</h3>
  <span class="ph" role="img" aria-label="Holiday nutcracker gifts" style="background:linear-gradient(#2a3a2a,#a82a2a)"></span>
  <h4>Twelve Favorite Holiday-Themed Gifts From Dreamvale Parks</h4>
  <div class="meta">November 12, 2014</div>
  <p>We've carried Dreamvale character nutcrackers for a few years at Dreamvale Parks. This year, we introduced some new sizes for figures… <span class="more">Read more »</span></p>
  <div class="showmore">Show More</div>
</section>
<section class="box half tech">
  <h3>Technology</h3>
  <span class="ph" role="img" aria-label="Vintage computer room in black and white" style="background:linear-gradient(#d0d0d0,#505050)"></span>
  <h4>Do You Remember Your Pre-Internet Self?</h4>
  <div class="meta">November 12, 2014</div>
  <p>The Internet, at least the modern version we know, turned 25 this year, and its effect on our lives simply cannot be understated… <span class="more">Read more »</span></p>
  <div class="showmore">Show More</div>
</section>

<section class="box latest">
  <h3>Latest Post</h3>
  <h4>Rolf Anderby Plans Theme Park</h4>
  <div class="row"><span class="ph" role="img" aria-label="Film cast at an event"></span><p><span class="meta">November 6, 2014</span><br>The film director will develop the project with Quiet Harrowgates composer Mick Morrowdale to imagine the rollercoasters… <span class="more">Read More »</span></p></div>
</section>

<section class="box featured">
  <h3>Featured Article</h3>
  <div class="gap"><span class="ph" role="img" aria-label="Woman on a coaster" style="background:linear-gradient(#c4a8a0,#5a4a6a)"></span><h4>Chatfield woman scores 100 millionth ride…</h4><div class="meta">August 6, 2014</div></div>
  <div><span class="ph" role="img" aria-label="Amusement park midway" style="background:linear-gradient(#9ec3e6,#c9a070)"></span><h4>Vote For Your Favorite Amusement Park</h4><div class="meta">August 5, 2014</div></div>
</section>

<section class="box advert">
  <h3>Advertising</h3>
  <div class="sky" role="img" aria-label="Car advertisement"><strong>PRESENTING LIMITED EDITION</strong><span>WITH 10 NEW SMART FEATURES</span><span class="btn">KNOW MORE</span></div>
</section>

<section class="box archive">
  <h3>Archive</h3>
  <ul><li><span>November 2014</span><span>2</span></li><li><span>October 2014</span><span>3</span></li><li><span>September 2014</span><span>1</span></li><li><span>August 2014</span><span>6</span></li><li><span>July 2014</span><span>4</span></li><li><span>April 2014</span><span>1</span></li></ul>
</section>

<section class="box tweets">
  <div class="hint">When talking about GustHarbor please use the hashtag<br><b>#GustHarbor</b></div>
  <div class="head"><span>Tweets</span><span class="meta">Follow</span></div>
  <div class="tweet"><b>GustHarbor.com</b> @gustharbor<br><span class="tag">#GustHarbor</span><br>Daily paper is out!</div>
  <div class="tweet"><b>GustHarbor.com</b> @gustharbor<br><span class="tag">#GustHarbor</span><br>Daily paper is out!</div>
  <div class="tweet"><b>GustHarbor.com</b> @gustharbor<br><span class="tag">#GustHarbor</span><br>Daily paper is out!</div>
  <div class="tweet"><b>GustHarbor.com</b> @gustharbor<br>The base of the lift of #Gale410 is ready</div>
  <div class="compose">Tweet to @gustharbor</div>
</section>

<section class="box video">
  <h3>Our Video</h3>
  <span class="ph" role="img" aria-label="Music video still"></span>
</section>

<section class="box login">
  <h3>Login</h3>
  <div class="field"><i></i><span>username</span></div>
  <div class="field"><i></i><span>password</span></div>
  <div class="act"><span class="btn">Log In</span><span>Remember Me</span></div>
</section>

<section class="box counter">
  <h3>Social Counter</h3>
  <div class="grid">
    <div class="cell"><i style="background:#f08a24"></i>RSS<br>Subscribe</div>
    <div class="cell"><i style="background:#3b5998"></i>Chatterly<br>2522 Fans</div>
    <div class="cell"><i style="background:#3aa0e0"></i>Chirpline<br>2362 Followers</div>
    <div class="cell"><i style="background:#d94a38"></i>Plexo+<br>22 followers</div>
    <div class="cell"><i style="background:#cb2027"></i>Pinwall<br>40 followers</div>
    <div class="cell"><i style="background:#c4302b"></i>Vidstream<br>58 Subscribers</div>
  </div>
</section>

<section class="box comments">
  <h3>Latest Comments</h3>
  <div class="cm"><span class="ph" style="background:#b34a4a" role="img" aria-label="Event photo"></span><h4>Rolf Anderby plans theme park with the Tinsmiths<br><span class="meta">November 8, 2014</span></h4></div>
  <div class="cm"><span class="ph" style="background:#7a9ac0" role="img" aria-label="Park rides"></span><h4>Crown Ridge Adding Two Rides And…<br><span class="meta">November 6, 2014</span></h4></div>
  <div class="cm"><span class="ph" style="background:#1a1a1a" role="img" aria-label="Haunt poster"></span><h4>Review: Knoll's Fright Farm Haunt 2014<br><span class="meta">October 17, 2014</span></h4></div>
  <div class="cm"><span class="ph" style="background:#5a6a8a" role="img" aria-label="Studio park"></span><h4>Marquee Studios Hollywood Invites Fans to Attend…</h4></div>
  <div class="cm"><span class="ph" style="background:#2a6aa0" role="img" aria-label="Aquarium tank"></span><h4>Deep Tide Aquarium – We checked out this…</h4></div>
  <div class="cm"><span class="ph" style="background:#8a6a3a" role="img" aria-label="Wooden coaster"></span><h4>Sixpeak Wonder Summit's 'Titanix' Roller Coaster…</h4></div>
  <div class="cm"><span class="ph" style="background:#6a8aa0" role="img" aria-label="Park skyline"></span><h4>Birch Point Is Hiring 300 People…<br><span class="meta">August 6, 2014</span></h4></div>
</section>

<section class="box follow">
  <h3>Follow Us</h3>
  <div class="grid">
    <span style="background:#3b5998"></span><span style="background:#3aa0e0"></span><span style="background:#d94a38"></span><span style="background:#f08a24"></span><span style="background:#cb2027"></span><span style="background:#c4302b"></span><span style="background:#ff0084"></span>
    <span style="background:#3b5998"></span><span style="background:#0077b5"></span><span style="background:#517fa4"></span><span style="background:#34526f"></span><span style="background:#555"></span><span style="background:#ea4c89"></span><span style="background:#1ab7ea"></span>
  </div>
</section>

<section class="box fb">
  <h3>Chatterly</h3>
  <div class="fbcard">
    <div class="top"><i></i><div><b>GustHarbor.com</b><br><span class="meta">Like</span></div></div>
    2,992 people like GustHarbor.com.
    <div class="faces"><span></span><span></span><span></span><span></span><span></span><span></span><span></span><span></span></div>
  </div>
</section>

<section class="box feed">
  <div class="bar">Find us on Chatterly</div>
  <div class="page"><i></i><div><b>GustHarbor.com</b><br><span class="meta">Like 2,926</span></div></div>
  <div class="post"><b style="font-size:12px">GustHarbor.com</b><br><span class="meta">November 15</span><br>Another section of lift hill track went up today for <span style="color:var(--blue)">#Gale410, Carolbreeze Amusement Park.</span><span class="ph" role="img" aria-label="Crane lifting coaster track"></span></div>
</section>

<div class="abs band"></div>
<div class="abs foot-ad"><span>DEAL SAGE<br><small>STYLISH HANDBAG COMBO</small></span><span class="bags" role="img" aria-label="Handbag product photos"></span><span style="color:var(--red)">DEAL PRICE ₹599/-</span></div>

<section class="abs newsletter">
  <h2>Newsletter Sign-Up!</h2>
  <div class="row"><div class="in">Enter your E-mail</div><div class="go">Subscribe</div></div>
</section>

<footer class="abs footer">
  <div class="about"><h5>About Us</h5><p>GustHarbor brings you news and information about amusement parks, theme parks, roller coasters and thrill rides. Here you will find up-to-date news and travel discounts on your favorite parks including Sixpeak, Birch Point, Maple Fair, Dreamvale World, Dreamvaleland, Marquee Studios Hollywood, Marquee Studios Orlando, Bosk Gardens Tampa and Bosk Gardens Williamsburg.</p></div>
  <div class="links"><h5>Link</h5><ul><li>Roller Coaster History</li><li>Timeline of Roller Coasters and Thrillrides</li><li>Glossary of Roller Coaster Terms</li><li>Headlines</li><li>Photos</li><li>Videos</li><li>Leisure</li><li>More</li></ul></div>
  <div class="contact"><h5>Contact Us</h5><span>Name</span><span>Email</span><span class="msg">Message</span><div class="btn">Submit</div></div>
  <div class="follows"><h5>Follow Us</h5><div class="grid"><span></span><span></span><span></span><span></span><span></span><span></span><span></span></div></div>
</footer>

<div class="abs totop"></div>
<div class="abs bottom">© 2014 by GustHarbor.com</div>

</body>
</html>
```